Luxury Eye Cream Label

Velmora Skin is developing a line of luxury dermatology creams designed to improve and treat various skin conditions and esthetic problems.
All creams are handmade by registered pharmacies according to patient needs, on the same day of the order. (meaning the creams are not premade. the creams are freshly made without any preservatives or stabilizers.)
The labels are two. One for the upper lid of an aluminum container 4.0 cm. in diameter containing company logo and description of the cream. The other one is for the bottom of the container 4.0 in diameter containing pharmacy information.
The label should convey professional, MD, and luxury feel.
(Upper Lid Label)
Logo of velmora skin
EYE CARE CREAM - intensive
Doctor Series
handmade . Doctor formulated . registered Pharmacy . highest ethical standards . (in a circular pattern on the label)
Ingredients: Marigold extract, Witch Hazel Distillate, Water, Glycerin, Stearyl Alcohol, Wheat Germ Oil, Polysorbate 60, Sesame Oil, Myristyl Myristate, Cetyl Alcohol, Sorbitan Stearate, Phenoxyethanol, Calendula Extract, Cornflower Extract, Sodium Alginate, Sodium Citrate, Mica, Vit. C, Vit. E.
Please, adhere to the above content, and dimension of the label of 4 cm in diameter. Also, please view it to scale. This is a relatively small container, aluminum ½ ounce (15ml) cream.
The Bottom of the Jar will have a label with the following information. This is obligatory, because of regulatory requirements for any product prepared by a pharmacy.
I understand that the space is limited. The background should be a lighter color, and the pharmacist will hand write the information (with a darker color marker).
EXTERNAL USE
Pharmacy: Pelaro, 18 Blvd. Ts. Orlinov, Sofia 1157, ph. 02 9473615
Rx No. Date
Patient Name age
Pharmacist Good until:
Please, view it to scale of 4 cm in diameter (which is the actual label of the Face Cream Intense), so you will have a better feeling of the design.
Thank you so much.

```html
<!DOCTYPE html>
<html lang="en">
<head>
<meta charset="utf-8">
<title>Velmora Skin – Eye Care Cream Labels</title>
<link rel="stylesheet" href="https://fonts.googleapis.com/css2?family=Cinzel:wght@400;500&family=Lato:wght@400;700&display=swap">
<style>
  :root {
    --page: #f6f4f3;
    --label-black: #0d0d0d;
    --silver-light: #f2f2f2;
    --silver-mid: #c9c9c9;
    --silver-dark: #8e8e8e;
    --ink: #1a1a1a;
    --ink-soft: #3a3a3a;
    --white: #ffffff;
  }
  * { box-sizing: border-box; margin: 0; padding: 0; }
  html, body { width: 1200px; height: 1200px; overflow: hidden; }
  body {
    background: var(--page);
    font-family: "Lato", sans-serif;
    position: relative;
  }
  .lid-label {
    position: absolute;
    left: 230px;
    top: 40px;
    width: 740px;
    height: 740px;
  }
  .lid-label svg { width: 100%; height: 100%; display: block; }
  .ring-text { font-family: "Lato", sans-serif; font-size: 33px; fill: var(--ink); letter-spacing: 0.5px; }
  .brand-name { font-family: "Lato", sans-serif; font-size: 54px; fill: var(--white); }
  .product-title { font-family: "Cinzel", serif; font-size: 50px; fill: var(--ink); }
  .product-variant { font-family: "Cinzel", serif; font-size: 22px; fill: var(--ink); letter-spacing: 9px; }
  .ingredients { font-family: "Lato", sans-serif; font-size: 16.5px; fill: var(--white); }

  .base-label {
    position: absolute;
    left: 320px;
    top: 830px;
    width: 560px;
    height: 300px;
    padding: 34px 44px;
    background: linear-gradient(180deg, var(--silver-light) 0%, #dcdcdc 55%, #ececec 100%);
    border: 1px solid var(--silver-mid);
    color: var(--ink-soft);
  }
  .base-label__heading { font-size: 24px; letter-spacing: 1px; margin-bottom: 10px; }
  .base-label__pharmacy { font-size: 21px; line-height: 1.35; margin-bottom: 14px; }
  .rx-table { border-collapse: collapse; width: 82%; }
  .rx-table td {
    border: 1.5px solid var(--silver-dark);
    font-size: 20px;
    padding: 3px 8px;
    height: 32px;
  }
</style>
</head>
<body>

<div class="lid-label">
  <svg viewBox="0 0 800 800" xmlns="http://www.w3.org/2000/svg">
    <defs>
      <linearGradient id="silverRim" x1="0" y1="0" x2="1" y2="1">
        <stop offset="0" stop-color="#f4f4f4"/>
        <stop offset="0.5" stop-color="#cfcfcf"/>
        <stop offset="1" stop-color="#efefef"/>
      </linearGradient>
      <linearGradient id="silverBand" x1="0" y1="0" x2="1" y2="0">
        <stop offset="0" stop-color="#b8b8b8"/>
        <stop offset="0.5" stop-color="#f0f0f0"/>
        <stop offset="1" stop-color="#b8b8b8"/>
      </linearGradient>
      <path id="ringPath" d="M400,748 A348,348 0 1,1 400,52 A348,348 0 1,1 400,748"/>
      <clipPath id="innerClip"><circle cx="400" cy="400" r="300"/></clipPath>
    </defs>

    <circle cx="400" cy="400" r="395" fill="url(#silverRim)" stroke="#a9a9a9" stroke-width="2"/>
    <text class="ring-text">
      <textPath href="#ringPath" startOffset="14" textLength="2160" lengthAdjust="spacing">Doctor Series • Handmade • Doctor formulated • Registered Pharmacy • Highest ethical standards •</textPath>
    </text>

    <circle cx="400" cy="400" r="306" fill="none" stroke="#9a9a9a" stroke-width="2"/>
    <circle cx="400" cy="400" r="300" fill="var(--label-black)"/>

    <g clip-path="url(#innerClip)">
      <circle cx="200" cy="222" r="22" fill="none" stroke="#ffffff" stroke-width="2.5"/>
      <text class="brand-name" x="420" y="240" text-anchor="middle">velmora skin</text>
      <line x1="160" y1="280" x2="640" y2="280" stroke="#bdbdbd" stroke-width="2"/>
      <rect x="95" y="290" width="610" height="130" fill="url(#silverBand)"/>
      <text class="product-title" x="400" y="352" text-anchor="middle">EYE CARE CREAM</text>
      <line x1="180" y1="370" x2="620" y2="370" stroke="#555" stroke-width="1.5"/>
      <text class="product-variant" x="400" y="402" text-anchor="middle">INTENSIVE</text>

      <text class="ingredients" text-anchor="middle">
        <tspan x="400" y="456">Ingredients: Marigold extract, Witch Hazel Distillate, Water, Glycerin,</tspan>
        <tspan x="400" y="480">Stearyl Alcohol, Wheat Germ Oil, Polysorbate 60, Sesame Oil,</tspan>
        <tspan x="400" y="504">Myristyl Myristate, Cetyl Alcohol, Sorbitan Stearate,</tspan>
        <tspan x="400" y="528">Phenoxyethanol, Calendula Extract, Cornflower</tspan>
        <tspan x="400" y="552">Extract, Sodium Alginate, Sodium Citrate,</tspan>
        <tspan x="400" y="576">Mica, Vit. C, Vit. E.</tspan>
      </text>
    </g>
  </svg>
</div>

<div class="base-label">
  <p class="base-label__heading">EXTERNAL USE</p>
  <p class="base-label__pharmacy">Pharmacy: Pelaro, 18 Blvd. Ts. Orlinov,<br>Sofia 1157, ph. 02 9473615</p>
  <table class="rx-table">
    <tr><td>Rx No. Date</td></tr>
    <tr><td>Patient Name age</td></tr>
    <tr><td>Pharmacist Good until:</td></tr>
  </table>
</div>

</body>
</html>
```